依頼概要
■依頼目的 / 概要
電子書籍Lumora本を出版いたしますので、
表紙デザイン作成をお願いいたします。

■納品物
下記での納品をお願い致します。

JPEG形式 及び PSD形式
横1600ピクセル x 縦2560ピクセル

■本の内容

<本のタイトル>
ソラノワ-SKY RING-
老職人に学んだ
はじめての家庭づくりのガイドブック

<著者名>
浅井徹郎

■デザイン要望
・本のタイトル / 著者名の反映をお願いします

デザインイメージ

・基本的に青系の色合い

・シンプルな背景にタイトル等のコピーを記載

・ターゲットは子どもを持つご両親。

・お子様の子育てに関する細かいノウハウというよりも、
最も要となる考え方をお伝えしています。

・信頼感のあるデザインを希望します。

<表現したいイメージなど>
・信頼感

<表現したくないイメージ>
・安っぽい
・嘘くさい
・大衆的

<利用画像について>
画像素材を使用される場合には、
商用利用可の素材をお願いします。

■その他
デザインを考えるのに必要な情報が他にございましたら、
お答えしますので、遠慮なくご連絡ください。

*添付ファイルは、過去電子書籍の表紙デザインです。
*ジャンルが異なりますので、デザインテイストは今回とは、異なります。
*あくまでも、表紙に出てくる要素(タイトルや著者名など)の参考としてご利用ください。

意図をしっかりとご理解いただき、
目につく素晴らしいデザインに仕上げていただきました。
ありがとうございます。

この度は応募いただきありがとうございました。
近いうちにまた同じく、表紙のデザインをお願いする予定です。
またご参加くださいませ。

```html
<!DOCTYPE html>
<html lang="ja">
<head>
<meta charset="utf-8">
<title>ソラノワ -SKY RING- 表紙</title>
<link rel="stylesheet" href="https://fonts.googleapis.com/css2?family=Noto+Sans+JP:wght@900&family=Shippori+Mincho:wght@500&family=Noto+Serif:wght@400;600&display=swap">
<style>
  :root {
    --navy: #1d2b7a;
    --band: #4a4d6f;
    --gold: #bca46a;
    --gold-soft: #a8925c;
    --white: #ffffff;
    --paper: #f4ecd8;
    --quill: #e4e6f0;
    --ink: #1a1a1a;
  }
  html, body {
    margin: 0;
    padding: 0;
    overflow: hidden;
    background: #ffffff;
  }
  .cover {
    position: relative;
    width: 749px;
    height: 1200px;
    background: var(--navy);
    overflow: hidden;
  }
  .border-band {
    position: absolute;
    background: var(--band);
  }
  .border-band--top { top: 8px; left: 8px; right: 8px; height: 14px; }
  .border-band--bottom { bottom: 8px; left: 8px; right: 8px; height: 14px; }
  .border-band--left { top: 8px; bottom: 8px; left: 8px; width: 14px; }
  .border-band--right { top: 8px; bottom: 8px; right: 8px; width: 14px; }
  .inner-frame {
    position: absolute;
    top: 32px; left: 30px; right: 30px; bottom: 32px;
    border: 1px solid var(--gold-soft);
  }
  .title {
    position: absolute;
    top: 64px;
    left: 0;
    width: 749px;
    margin: 0;
    text-align: center;
    font-family: "Noto Sans JP", sans-serif;
    font-weight: 900;
    font-size: 136px;
    letter-spacing: 4px;
    color: var(--gold);
    line-height: 1;
  }
  .subtitle {
    position: absolute;
    top: 222px;
    left: 0;
    width: 749px;
    font-family: "Noto Serif", serif;
    font-weight: 600;
    font-size: 46px;
    line-height: 56px;
    color: var(--gold);
    letter-spacing: 1px;
    display: flex;
    justify-content: center;
    align-items: center;
    gap: 18px;
  }
  .subtitle .dash { display: inline-block; width: 68px; height: 2px; background: var(--gold); }
  .quill-area {
    position: absolute;
    top: 352px;
    left: 352px;
    width: 46px;
    height: 46px;
    background: var(--quill);
    opacity: 0.85;
  }
  .author {
    position: absolute;
    top: 428px;
    left: 0;
    width: 749px;
    text-align: center;
    font-family: "Shippori Mincho", serif;
    font-weight: 500;
    font-size: 64px;
    letter-spacing: 16px;
    text-indent: 16px;
    color: var(--white);
    line-height: 1;
  }
  .author-rule {
    position: absolute;
    top: 506px;
    left: 252px;
    width: 245px;
    height: 1px;
    background: var(--white);
  }
  .author-roman {
    position: absolute;
    top: 512px;
    left: 0;
    width: 749px;
    text-align: center;
    font-family: "Noto Serif", serif;
    font-size: 19px;
    letter-spacing: 2px;
    color: var(--white);
  }
  .book-area {
    position: absolute;
    left: 86px;
    top: 686px;
    width: 578px;
    height: 420px;
    background: var(--paper);
  }
  .book-copy {
    position: absolute;
    left: 142px;
    top: 752px;
    margin: 0;
    font-family: "Shippori Mincho", serif;
    font-weight: 500;
    font-size: 37px;
    line-height: 80px;
    letter-spacing: 3px;
    color: var(--ink);
  }
</style>
</head>
<body>
<div class="cover">
  <div class="border-band border-band--top" role="img" aria-label="文字と星が繰り返す金色の縁取り模様"></div>
  <div class="border-band border-band--bottom" role="img" aria-label="文字と星が繰り返す金色の縁取り模様"></div>
  <div class="border-band border-band--left" role="img" aria-label="文字と星が繰り返す金色の縁取り模様"></div>
  <div class="border-band border-band--right" role="img" aria-label="文字と星が繰り返す金色の縁取り模様"></div>
  <div class="inner-frame"></div>

  <h1 class="title">ソラノワ</h1>
  <div class="subtitle"><span class="dash"></span>SKY RING<span class="dash"></span></div>

  <div class="quill-area" role="img" aria-label="白い羽ペンの飾り"></div>
  <div class="author">浅井徹郎</div>
  <div class="author-rule"></div>
  <div class="author-roman">asai tetsuro</div>

  <div class="book-area" role="img" aria-label="開いた本のイラスト"></div>
  <p class="book-copy">老職人に学んだ<br>はじめての家庭づくりの<br>ガイドブック</p>
</div>
</body>
</html>
```